Pellwick Healthcare Booklet 2016

Pellwick Healthcare is a multi-specialty Practice in Midtown Manhattan offering advanced care in multiple areas of medicine. See our table of contents (PDF Uploaded)
Our designed booklet should be clean, easy to read, contemporary, high-end and elegant.
We need a general theme, Layout for cover and templates for internal.
We are entertaining the idea of two different sizes
8 x 10
or
11 x 8.5
Our tagline " The Future of Medicine is Here"
We will provide all the text content
The link to our website
www.PellwickHC.example
Uploaded files are as follows.. Logo, Our Team Photo and the PDF listing the table of contents.

```html
<!DOCTYPE html>
<html lang="en">
<head>
<meta charset="utf-8">
<title>Pellwick Healthcare Booklet</title>
<link href="https://fonts.googleapis.com/css2?family=Open+Sans:wght@400;600;700&display=swap" rel="stylesheet">
<style>
  :root {
    --navy: #3a3d63;
    --navy-deep: #2f3255;
    --page-white: #ffffff;
    --cover-grey: #e4e5e8;
    --text-grey: #6d6f80;
    --backdrop: #d2d3d6;
    --scrub-light: #9fb3d6;
    --scrub-mid: #7b8fbd;
    --room-tone: #c9c6c0;
  }
  * { margin: 0; padding: 0; box-sizing: border-box; }
  html, body {
    width: 1200px; height: 857px; overflow: hidden;
    background: var(--backdrop);
    font-family: "Open Sans", Arial, sans-serif;
  }
  .spread {
    position: absolute; left: 100px; top: 100px;
    width: 1000px; height: 657px;
    display: flex;
    box-shadow: 0 6px 24px rgba(0,0,0,.18);
  }
  .page { position: relative; width: 500px; height: 657px; overflow: hidden; }
  .page svg.layer { position: absolute; inset: 0; }

  /* back cover */
  .back-cover { background: var(--page-white); }
  .team-banner {
    position: absolute; left: 0; top: 0; width: 500px; height: 150px;
    background: linear-gradient(90deg, var(--room-tone), var(--scrub-light) 45%, #e8e6e2 80%, var(--scrub-mid));
    border-bottom: 5px solid var(--navy);
  }
  .testimonial { position: absolute; left: 62px; top: 230px; width: 360px; }
  .testimonial h2 { color: var(--navy); font-weight: 700; font-size: 30px; line-height: 1.1; margin-bottom: 12px; }
  .testimonial p { color: var(--text-grey); font-size: 13.5px; line-height: 1.45; }
  .contact { position: absolute; left: 62px; top: 510px; color: #fff; }
  .brand { display: flex; align-items: center; gap: 10px; margin-bottom: 14px; }
  .brand-dot { width: 26px; height: 26px; border-radius: 50%; background: #c9a24a; }
  .brand-name { font-weight: 600; font-size: 13px; letter-spacing: .5px; text-transform: uppercase; }
  .contact .address { font-size: 12.5px; margin-bottom: 4px; }
  .contact .phone { font-size: 24px; font-weight: 600; letter-spacing: .5px; }
  .back-url {
    position: absolute; left: 0; right: 0; bottom: 22px; text-align: center;
    color: #c8cadb; font-size: 9px; letter-spacing: 3px;
  }

  /* front cover */
  .front-cover { background: var(--cover-grey); }
  .front-brand {
    position: absolute; top: 32px; left: 0; right: 0;
    display: flex; justify-content: center; align-items: center; gap: 10px;
    color: var(--navy);
  }
  .tagline { position: absolute; top: 528px; left: 0; right: 0; text-align: center; color: var(--navy); }
  .tagline .lead { display: block; font-weight: 700; font-size: 30px; line-height: 1.1; }
  .tagline .rest { display: block; font-size: 26px; line-height: 1.15; }
  .front-band {
    position: absolute; left: 0; right: 0; bottom: 0; height: 34px;
    background: var(--navy);
    color: #c8cadb; font-size: 9px; letter-spacing: 3px;
    display: flex; align-items: center; justify-content: center;
  }
</style>
</head>
<body>
<div class="spread">
  <section class="page back-cover">
    <div class="team-banner" role="img" aria-label="Photo of the medical team standing together in the clinic"></div>
    <svg class="layer" width="500" height="657" viewBox="0 0 500 657" aria-hidden="true">
      <path d="M0 150 L500 150 L500 158 C 350 175, 150 175, 0 165 Z" fill="var(--navy)"/>
      <path d="M0 395 C 150 400, 330 440, 500 470 L500 657 L0 657 Z" fill="var(--navy)"/>
    </svg>
    <div class="testimonial">
      <h2>Testimonial</h2>
      <p>You saved me - without you I could never have completed my book. You are a true healer in every sense of the word. Thanks for being there when I needed it the most!!</p>
    </div>
    <div class="contact">
      <div class="brand"><span class="brand-dot"></span><span class="brand-name">Pellwick Healthcare</span></div>
      <p class="address">120 Larkmoor Street New York, NY 10099</p>
      <p class="phone">212-555-0148</p>
    </div>
    <p class="back-url">www.PellwickHC.example</p>
  </section>

  <section class="page front-cover">
    <div class="front-brand"><span class="brand-dot"></span><span class="brand-name">Pellwick Healthcare</span></div>
    <svg class="layer" width="500" height="657" viewBox="0 0 500 657">
      <defs>
        <linearGradient id="teamTones" x1="0" y1="0" x2="0" y2="1">
          <stop offset="0" stop-color="var(--room-tone)"/>
          <stop offset=".45" stop-color="var(--scrub-light)"/>
          <stop offset="1" stop-color="var(--scrub-mid)"/>
        </linearGradient>
      </defs>
      <g fill="var(--navy)">
        <rect x="155" y="95" width="190" height="410" rx="26"/>
        <rect x="55" y="195" width="390" height="150" rx="26"/>
      </g>
      <g fill="url(#teamTones)" role="img" aria-label="Group photo of the medical team in scrubs, framed in a cross shape">
        <rect x="161" y="101" width="178" height="398" rx="21"/>
        <rect x="61" y="201" width="378" height="138" rx="21"/>
      </g>
    </svg>
    <h1 class="tagline"><span class="lead">The Future</span><span class="rest">of Medicine is Here</span></h1>
    <div class="front-band">www.PellwickHC.example</div>
  </section>
</div>
</body>
</html>
```